Minimalist Modern Business Card Design, open to ideas, or cleaner version of provided files, but what logo & logo colors (with some black) as shown in files, and info for back shown in files as well.

```html
<!DOCTYPE html>
<html lang="en">
<head>
<meta charset="utf-8">
<title>Trailhand Truck Care – Business Card</title>
<link href="https://fonts.googleapis.com/css2?family=Montserrat:wght@500&family=Lato:wght@400;700&display=swap" rel="stylesheet">
<style>
  :root {
    --navy: #26276f;
    --ink: #111111;
    --paper: #ffffff;
    --backdrop: #e4e4e4;
  }
  * { box-sizing: border-box; margin: 0; padding: 0; }
  html, body {
    width: 850px;
    height: 1200px;
    overflow: hidden;
    background: var(--backdrop);
  }
  .sheet {
    width: 850px;
    height: 1200px;
    display: flex;
    flex-direction: column;
    align-items: center;
    justify-content: center;
    gap: 120px;
  }
  .card {
    position: relative;
    width: 700px;
    height: 400px;
    background: var(--paper);
    box-shadow: 0 6px 18px rgba(0,0,0,0.12);
  }

  /* Front */
  .brand {
    position: absolute;
    top: 118px;
    left: 0;
    right: 0;
    display: flex;
    align-items: center;
    justify-content: center;
    gap: 16px;
  }
  .brand-square {
    width: 30px;
    height: 30px;
    background: var(--navy);
  }
  .brand-name {
    font-family: "Lato", sans-serif;
    font-weight: 700;
    font-size: 34px;
    line-height: 1;
    color: var(--navy);
    white-space: nowrap;
  }
  .contact-row {
    position: absolute;
    top: 272px;
    left: 0;
    right: 0;
    display: flex;
    justify-content: center;
    align-items: center;
    font-family: "Lato", sans-serif;
  }
  .person {
    text-align: right;
    padding-right: 22px;
  }
  .person-name {
    font-family: "Montserrat", sans-serif;
    font-weight: 500;
    font-size: 22px;
    color: var(--navy);
    line-height: 1.1;
  }
  .person-title {
    font-weight: 700;
    font-size: 16px;
    color: var(--ink);
  }
  .divider {
    width: 1.5px;
    height: 42px;
    background: var(--navy);
  }
  .details {
    padding-left: 22px;
    font-size: 16px;
    line-height: 1.6;
    color: var(--navy);
  }
  .details b { color: var(--ink); }

  /* Back */
  .card-back {
    display: flex;
    padding: 80px 0 0 61px;
  }
  .column {
    display: flex;
    gap: 16px;
    height: 241px;
  }
  .column-services { width: 349px; }
  .band {
    width: 35px;
    height: 241px;
    background: var(--navy);
    display: flex;
    align-items: center;
    justify-content: center;
  }
  .band-label {
    writing-mode: vertical-rl;
    transform: rotate(180deg);
    font-family: "Lato", sans-serif;
    font-size: 16px;
    letter-spacing: 1.5px;
    color: var(--paper);
    white-space: nowrap;
  }
  .list {
    list-style: none;
    font-family: "Lato", sans-serif;
    font-size: 15px;
    color: var(--navy);
    display: flex;
    flex-direction: column;
    justify-content: space-between;
    height: 241px;
  }
  .list li {
    position: relative;
    padding-left: 18px;
    line-height: 1;
    white-space: nowrap;
  }
  .list li::before {
    content: "";
    position: absolute;
    left: 0;
    top: 3px;
    border-left: 8px solid var(--navy);
    border-top: 5px solid transparent;
    border-bottom: 5px solid transparent;
  }
</style>
</head>
<body>
<main class="sheet">
  <section class="card card-front" aria-label="Card front">
    <div class="brand">
      <span class="brand-square" aria-hidden="true"></span>
      <span class="brand-name">Trailhand Truck Care</span>
    </div>
    <div class="contact-row">
      <div class="person">
        <div class="person-name">MY NAME</div>
        <div class="person-title">President</div>
      </div>
      <span class="divider" aria-hidden="true"></span>
      <div class="details">
        <div><b>C.</b> 123-456-7890</div>
        <div><b>E.</b> info@trailhandtruckcare.com</div>
      </div>
    </div>
  </section>

  <section class="card card-back" aria-label="Card back">
    <div class="column column-services">
      <div class="band"><span class="band-label">SERVICES INCLUDE</span></div>
      <ul class="list">
        <li>Shop &amp; Mobile</li>
        <li>DOT &amp; BIT Inspections</li>
        <li>All Maintenance &amp; Repairs</li>
        <li>Check Engine Lights</li>
        <li>Diags, Regens &amp; Programming</li>
        <li>Full Dealer Software Capabilities</li>
        <li>PM &amp; Compliance Tracking</li>
        <li>App-Based Billing &amp; Live Updates</li>
        <li>Dealer Certified Techs</li>
        <li>Night Servicing to Avoid Downtime</li>
      </ul>
    </div>
    <div class="column column-specialties">
      <div class="band"><span class="band-label">SPECIALIZING IN</span></div>
      <ul class="list">
        <li>Heavy &amp; Medium Duty</li>
        <li>Crestline</li>
        <li>Ozura</li>
        <li>Kiro</li>
        <li>Pinebuilt</li>
        <li>Haulmaster</li>
        <li>Kenfield</li>
        <li>Alderton</li>
        <li>After Treatment</li>
        <li>And More</li>
      </ul>
    </div>
  </section>
</main>
</body>
</html>
```